V.Crest Gin - Bottle label Design

We are manufacturers of Gin in South Africa.
The name of our Gin is V.Crest Gin with Q standing for Vukhamba, a Xhosa Village in the region of Eastern Cape.

We would like our brand to depict the following (really the focus of Gold on it)
> Prosperity of the place
> Wealth of the place, land, material or in the people
> Gold rush, potential, hope

As the brand matures, we would like to have campaigns with it. See ideas below:
> V.Crest Premium
> Red dusk edition
Limited edition will be released every year
- V.Crest entabeni (location)
- V.Crest elwandle (location)

> Each batch of bottles with focus on a specific area/location in Vukhamba. One that is known and will be highlighted on the map design of the bottle.
Bottles based on landmarks in Vukhamba and landmark design in the Big V.

Below we tried but we are not where we really want to be in terms of Gin Bottle elegance.

Target Market(s)

Target market is the young crowd. Young Xhosa men and women working really hard to get their goals. Positive thinkers. Elegant. Fresh. Bold. Age from 24 to 45. People who enjoy quality products.

Industry/Entity Type

Beverage Industry. Craft Gin.

Font styles to use
Sans Serif
Decorative

Colors
FFF300
FFF600
FEFA6F
FFFEC7
FFFEE8
FFC000
F8CF3A
FAE287
FDF2CF
FEFAEE

Requirements
Must have
• Gold colour as a theme. Try and make the background textured.

```html
<!DOCTYPE html>
<html lang="en">
<head>
<meta charset="utf-8">
<title>V.Crest Gin – Bottle Label</title>
<link rel="stylesheet" href="https://fonts.googleapis.com/css2?family=Poppins:wght@100;200;600;700;800&display=swap">
<style>
  :root {
    --stage: #e9e9e7;
    --paper: #ffffff;
    --paper-warm: #f3efe6;
    --ink: #111111;
    --gold: #c9861c;
    --gold-deep: #b06d12;
    --sepia-light: #cfc2a6;
    --sepia-mid: #a8987a;
    --sepia-dark: #5e5443;
    --dots: #333333;
  }
  * { box-sizing: border-box; margin: 0; padding: 0; }
  html, body {
    width: 1200px; height: 833px; overflow: hidden;
    background: var(--stage);
    font-family: "Poppins", sans-serif;
    color: var(--ink);
  }
  .label {
    position: absolute; left: 230px; top: 22px;
    width: 740px; height: 788px;
    background:
      radial-gradient(ellipse 60% 28% at 50% 22%, var(--paper-warm) 0%, rgba(243,239,230,0.6) 55%, rgba(255,255,255,0) 100%),
      var(--paper);
    overflow: hidden;
  }
  .label__texture { position: absolute; left: 0; top: 0; width: 740px; height: 320px; }

  .tagline-top {
    position: absolute; left: 0; right: 0; top: 36px;
    display: flex; align-items: center; justify-content: center; gap: 14px;
    font-size: 12.5px; font-weight: 600; letter-spacing: 7px;
  }
  .tagline-top__rule { width: 46px; height: 2px; background: var(--gold); }

  .brand-name {
    position: absolute; left: 0; right: 0; top: 150px;
    text-align: center;
    font-size: 82px; font-weight: 800; letter-spacing: 10px;
    line-height: 1;
  }

  .landscape {
    position: absolute; left: 27px; top: 313px; width: 685px; height: 292px;
    background: linear-gradient(180deg,
      var(--sepia-light) 0%, var(--sepia-mid) 22%, #8f806a 38%,
      var(--sepia-mid) 60%, var(--sepia-dark) 82%, #7d705c 100%);
  }

  .specs { position: absolute; left: 45px; top: 626px; width: 648px; height: 87px; }
  .specs__gin {
    position: absolute; left: 0; top: 0; width: 242px; height: 87px;
    display: flex; align-items: center; justify-content: center;
    font-size: 84px; font-weight: 100; letter-spacing: 18px; line-height: 1;
    padding-left: 18px;
  }
  .specs__origin, .specs__abv, .specs__volume {
    position: absolute; display: flex; align-items: center; justify-content: center;
    font-weight: 700; font-size: 25px; line-height: 1;
  }
  .specs__origin { left: 242px; top: 0; width: 406px; height: 42px; font-size: 24px; }
  .specs__abv { left: 242px; top: 42px; width: 216px; height: 45px; }
  .specs__volume { left: 458px; top: 42px; width: 190px; height: 45px; }
  .specs__lines { position: absolute; left: 0; top: 0; }

  .tagline-bottom {
    position: absolute; left: 0; right: 0; top: 722px;
    text-align: center; font-size: 15.3px; font-weight: 700; white-space: nowrap;
  }
  .gold-band {
    position: absolute; left: 27px; top: 758px; width: 685px; height: 6px;
    background: linear-gradient(90deg, var(--gold-deep), var(--gold), var(--gold-deep));
  }
</style>
</head>
<body>
  <main class="label">
    <svg class="label__texture" width="740" height="320" aria-hidden="true">
      <defs>
        <pattern id="grain" width="14" height="14" patternUnits="userSpaceOnUse">
          <circle cx="2" cy="3" r="0.7" fill="#b9ae98" opacity="0.35"/>
          <circle cx="9" cy="8" r="0.6" fill="#a99c84" opacity="0.3"/>
          <circle cx="5" cy="12" r="0.5" fill="#c4b9a3" opacity="0.35"/>
          <circle cx="12" cy="2" r="0.5" fill="#b3a78f" opacity="0.25"/>
        </pattern>
        <radialGradient id="grainFade" cx="50%" cy="45%" r="55%">
          <stop offset="0" stop-color="#fff" stop-opacity="1"/>
          <stop offset="1" stop-color="#fff" stop-opacity="0"/>
        </radialGradient>
        <mask id="grainMask"><rect width="740" height="320" fill="url(#grainFade)"/></mask>
      </defs>
      <rect width="740" height="320" fill="url(#grain)" mask="url(#grainMask)"/>
    </svg>

    <div class="tagline-top">
      <span class="tagline-top__rule"></span>
      <span>PREMIUM QUALITY</span>
      <span class="tagline-top__rule"></span>
    </div>

    <h1 class="brand-name">V.CREST</h1>

    <div class="landscape" role="img" aria-label="Sepia photograph of the Vukhamba valley: rolling hills, village houses, fenced fields and sacks stacked on the grass in the foreground"></div>

    <section class="specs">
      <svg class="specs__lines" width="648" height="87" aria-hidden="true">
        <g stroke="var(--dots)" stroke-width="2" stroke-dasharray="2 3" fill="none">
          <line x1="0" y1="1" x2="648" y2="1"/>
          <line x1="0" y1="86" x2="648" y2="86"/>
          <line x1="242" y1="42" x2="648" y2="42"/>
          <line x1="242" y1="1" x2="242" y2="86"/>
          <line x1="458" y1="42" x2="458" y2="86"/>
        </g>
      </svg>
      <div class="specs__gin">GIN</div>
      <div class="specs__origin">MADE IN THE EASTERN CAPE</div>
      <div class="specs__abv">37.5% ALC</div>
      <div class="specs__volume">750ML</div>
    </section>

    <p class="tagline-bottom">TRIPLE DISTRILLED WITH THE RICH &amp; AROMATIC TASTE OF THE VUKHAMBA REGION</p>

    <div class="gold-band"></div>
  </main>
</body>
</html>
```